Morvek Menu

Hi there,
My restaurant called "Morvek" means Spice in hebrew.
We are middle eastern restaurant that specialist in dips,salads and hot bread baked on the spot and charcoal grilled meat skewers
The restaurant is pretty casual and the atmosphere is nice and customers feels like home.
on www.morvek.com.au you can see photos of the restaurant and the food.
ill add up the menus that i would like to be design please and the logo that is on the front of the shop is been add up
thank you

Target Market(s)

The regulars of the restaurant is jewish/israelis

Industry/Entity Type

Restaurant

```html
<!DOCTYPE html>
<html lang="en">
<head>
<meta charset="utf-8">
<title>Morvek Menu</title>
<link href="https://fonts.googleapis.com/css2?family=Jura:wght@400;500&family=Didact+Gothic&display=swap" rel="stylesheet">
<style>
  :root {
    --ink: #1c1c1c;
    --paper: #ffffff;
    --frame: #d6d6d6;
    --header-dark: #141414;
    --header-mid: #2c2c2c;
    --header-text: #ffffff;
  }
  * { box-sizing: border-box; margin: 0; padding: 0; }
  html, body { width: 848px; height: 1200px; overflow: hidden; }
  body {
    background: var(--frame);
    font-family: "Jura", sans-serif;
    color: var(--ink);
    position: relative;
  }
  .menu-sheet {
    position: absolute; left: 12px; top: 0; width: 824px; height: 1188px;
    background: var(--paper);
  }
  .masthead {
    position: absolute; left: 0; top: 0; width: 848px; height: 213px;
    background: radial-gradient(ellipse at 50% 30%, var(--header-mid), var(--header-dark) 75%);
  }
  .brand-name {
    position: absolute; left: 0; right: 0; top: 22px;
    text-align: center; color: var(--header-text);
    font-family: "Didact Gothic", sans-serif; font-size: 76px; line-height: 1;
  }
  .column { position: absolute; width: 328px; }
  .column.left { left: 59px; }
  .column.right { left: 457px; }
  .section { position: absolute; left: 0; width: 100%; }
  .section-title {
    position: relative; margin-left: 11px; width: 308px; height: 32px;
    border: 2px solid var(--ink);
    font-family: "Jura", sans-serif; font-weight: 500; font-size: 22px;
    text-align: center; line-height: 28px; white-space: nowrap;
  }
  .section-title::before, .section-title::after {
    content: ""; position: absolute; top: 3px; width: 6px; height: 22px;
    border: 2px solid var(--ink);
  }
  .section-title::before { left: 3px; border-left: none; }
  .section-title::after { right: 3px; border-right: none; }
  .note { text-align: center; font-size: 14.5px; line-height: 19px; white-space: nowrap; }
  .items { list-style: none; font-size: 15px; line-height: 19px; white-space: nowrap; }
  .item { display: flex; align-items: baseline; }
  .item .leader { flex: 1; border-bottom: 1px dotted var(--ink); margin: 0 2px; transform: translateY(-4px); }
  .item-detail { font-size: 13.5px; line-height: 19px; padding-left: 16px; }
  .choices {
    display: grid; grid-template-columns: 196px 150px; width: 360px;
    padding-left: 12px; font-size: 15px; line-height: 19px; list-style: none; white-space: nowrap;
  }
  .rule-v { position: absolute; left: 425px; top: 345px; width: 2px; height: 480px; background: var(--ink); }
  .rule-h { position: absolute; left: 184px; top: 944px; width: 481px; height: 2px; background: var(--ink); }
</style>
</head>
<body>
<div class="menu-sheet"></div>
<header class="masthead"><div class="brand-name">Morvek</div></header>

<div class="rule-v"></div>
<div class="rule-h"></div>

<div class="column left">
  <section class="section" style="top:270px">
    <h2 class="section-title">Starters</h2>
    <ul class="items" style="margin-top:17px">
      <li class="item">Moroccan Beef Cigars<span class="leader"></span>$11.00</li>
      <li class="item-detail">(3 per serve)</li>
      <li class="item">Pan Fried Mushrooms and Onions<span class="leader"></span>$8.00</li>
      <li class="item">Lamb Kibbeh &amp; Pinenuts<span class="leader"></span>$7.50</li>
      <li class="item-detail">(3 per serve)</li>
      <li class="item">Falafel Balls<span class="leader"></span>$5.00</li>
      <li class="item">Fried Cauliflower<span class="leader"></span>$8.00</li>
    </ul>
  </section>

  <section class="section" style="top:491px">
    <h2 class="section-title">Hummus Plate</h2>
    <p class="note" style="margin-top:9px">Served with 1 Laffa and Mixed Pickles</p>
    <ul class="items" style="margin-top:6px">
      <li class="item">Masabacha<span class="leader"></span>$11.90</li>
      <li class="item-detail">(Served with Tahini and whole Chickpeas)</li>
      <li class="item">Ful<span class="leader"></span>$14.90</li>
      <li class="item-detail">(served with warm, crushed Fava Beans)</li>
      <li class="item">Mushroom<span class="leader"></span>$14.90</li>
      <li class="item-detail">(served with Pan Fried Mushrooms)</li>
      <li class="item">Basar<span class="leader"></span>$16.50</li>
      <li class="item-detail">(served with Mince Meat)</li>
    </ul>
  </section>

  <section class="section" style="top:726px">
    <h2 class="section-title">Salads &amp; Dips Platter</h2>
    <ul class="items" style="margin-top:17px">
      <li class="item">3 Choices &amp; Laffa<span class="leader"></span>$15.00</li>
      <li class="item">6 choices &amp; 2 Laffa<span class="leader"></span>$28.00</li>
    </ul>
    <ul class="choices" style="margin-top:9px">
      <li>-Hummus</li><li>-Moroccan Carrot</li>
      <li>-Baba Ganoush</li><li>-Roasted Beetroot</li>
      <li>-White Cabbage</li><li>-Turkish Dip</li>
      <li>-Chatzilim (Fried Eggplant)</li><li>-Mixed Pickles</li>
      <li>-Noa's Corn Salad</li><li>-Tahini</li>
    </ul>
  </section>

  <section class="section" style="top:985px">
    <h2 class="section-title">Kids Meals</h2>
    <p class="note" style="margin-top:9px">(10 and under only)</p>
    <ul class="items">
      <li class="item">Schnitzel plate<span class="leader"></span>$10.00</li>
      <li class="item-detail">(with chips and Israeli Salad)</li>
      <li class="item">Falafel Plate<span class="leader"></span>$9.00</li>
      <li class="item-detail">(with chips and Israeli Salad)</li>
    </ul>
  </section>
</div>

<div class="column right">
  <section class="section" style="top:270px">
    <h2 class="section-title">Israeli Lunch Tasting Plate</h2>
    <p class="note" style="margin-top:9px">All tasting plates include a Chef's<br>Selection of 4 Salads &amp; Dips and Laffa</p>
    <ul class="items">
      <li class="item">Chicken Shashlik Plate<span class="leader"></span>$10.00</li>
      <li class="item">Lamb Shashlik Plate<span class="leader"></span>$11.50</li>
      <li class="item">Kebab (Kofta) Shashlik Plate<span class="leader"></span>$14.90</li>
      <li class="item">Chicken Liver Plate $9.50<span class="leader"></span>$16.50</li>
      <li class="item">Schnitzel Plate<span class="leader"></span>$11.00</li>
      <li class="item">Falafel Plate<span class="leader"></span>$11.00</li>
    </ul>
  </section>

  <section class="section" style="top:491px">
    <h2 class="section-title">Wraps</h2>
    <p class="note" style="margin-top:9px">Fresh Laffa wrap with Hummus,<br>Tahini, Israeli salad<br>&amp; Mixed Pickles (Chilli optional)</p>
    <ul class="items" style="margin-top:10px">
      <li class="item">Falafel wrap<span class="leader"></span>$12.00</li>
      <li class="item">Chicken wrap<span class="leader"></span>$14.00</li>
      <li class="item">Schnitzel wrap<span class="leader"></span>$14.00</li>
      <li class="item">Kofta wrap<span class="leader"></span>$14.00</li>
      <li class="item">Lamb wrap<span class="leader"></span>$15.00</li>
    </ul>
  </section>

  <section class="section" style="top:727px">
    <h2 class="section-title">Individual Shashlik</h2>
    <p class="note" style="margin-top:18px">(1 Per serve)</p>
    <ul class="items" style="margin-top:7px">
      <li class="item">Chicken<span class="leader"></span>$10.00</li>
      <li class="item">Lamb<span class="leader"></span>$11.50</li>
      <li class="item">Kebab (Kofta) Shashlik<span class="leader"></span>$10.00</li>
      <li class="item">Chicken Liver<span class="leader"></span>$9.50</li>
      <li class="item">Schnitzel<span class="leader"></span>$11.00</li>
    </ul>
  </section>

  <section class="section" style="top:985px">
    <h2 class="section-title">Sides</h2>
    <ul class="items" style="margin-top:26px">
      <li class="item">Israeli Salad<span class="leader" style="margin-right:20px"></span>$10.00</li>
      <li class="item">Chips<span class="leader" style="margin-right:20px"></span>$8.00</li>
      <li class="item">Laffa<span class="leader" style="margin-right:20px"></span>$2.50</li>
      <li class="item">Pickles<span class="leader" style="margin-right:20px"></span>$6.00</li>
    </ul>
  </section>
</div>
</body>
</html>
```